Creation of website design for digital SAAS service for congresses, lectures and training

We are a startup in southern Germany that wants to prepare the digital bridge for all events so that the listener of a lecture or congress can digitally save the presentations and their notes. As a result, he is involved in the lecture much more intensively and will benefit from it. He can then use the app to ask the speaker / organizer to call you back using one of the picked slides. These are the leads that are generated from the events. It is a subscription model for the organizer or speakers so that he generates better results and more leads from his event. The application is running productively and can be used as a demo with a mobile phone at https://dorvane.net/demosession.html. Simply scan the QR code and pick the slides you like.
The website is a bit gruesome ..... that's why I need YOU!

The logo is Lumbo - our maksottchen, because he picks and saves the exciting slides from the presentation .....

The designer can get a free trial account for a month to get to know the app. Ends automatically!
https://app.dorvane.net/subscription/plans

Target Market(s)

Trade fair organizers, congress organizers, product management, hotel chains, associations, schools, universities, marketing organizations

Font styles to use
Sans Serif

Requirements
Must have
• The customer group are, on the one hand, marketing and sales professionals who should book the service for their customers and prospects so that more leads come from the events.
The login for the service can be done on any internet-enabled device with a browser.
Legal requirements regarding options for cookies and terms and conditions
Multilingualism DE and EN would then have to be considered technically.
The whole thing should then run on a wordpress version 5.41.
If images / photos are used, the copyright question must be clarified - what costs arise from the use and how is this to be documented if necessary.
Nice to have
• Maybe someone also creates an animation that explains the picking process nicely ... and maps the two user groups. Everyone should find themselves
Should not have
• Bad design and layout - I can top that myself!

```html
<!DOCTYPE html>
<html lang="de">
<head>
<meta charset="utf-8">
<title>Dorvane – Für die Picker</title>
<link href="https://fonts.googleapis.com/css2?family=Montserrat:wght@400;600;700;800&family=Open+Sans:wght@400;600;700&display=swap" rel="stylesheet">
<style>
:root{
  --green:#2f9e5e;
  --green-light:#3fb470;
  --green-pale:#e9f6ee;
  --pink:#f0567a;
  --pink-pale:#fdeef1;
  --ink:#222629;
  --text:#5e6469;
  --muted:#9aa0a5;
  --line:#e3e6e8;
  --grey-bg:#f6f7f8;
  --footer:#262a2d;
  --footer-bottom:#1d2022;
  --white:#ffffff;
}
*{box-sizing:border-box;margin:0;padding:0}
html,body{width:1200px;height:4344px;overflow:hidden}
body{font-family:"Open Sans",Arial,sans-serif;color:var(--text);background:var(--white);position:relative;font-size:13px;line-height:1.6}
h1,h2,h3,h4,.brand,.btn,.price{font-family:"Montserrat",Arial,sans-serif}
.abs{position:absolute}
.btn{display:inline-block;font-size:10px;font-weight:700;letter-spacing:.5px;text-transform:uppercase;color:var(--white);border-radius:3px;padding:9px 18px}
.btn-pink{background:var(--pink)}
.btn-green{background:var(--green)}
.label{font-size:10px;color:var(--green);letter-spacing:.5px}
.center{text-align:center}

/* nav */
.site-nav{top:0;left:0;width:1200px;height:100px;background:var(--white);display:flex;align-items:center;padding:0 240px}
.brand{display:flex;align-items:center;gap:8px;font-size:22px;font-weight:800;color:var(--ink)}
.brand-dot{width:22px;height:22px;border-radius:50%;background:var(--green)}
.nav-links{margin-left:auto;display:flex;gap:28px;align-items:center;font-size:12px;color:var(--ink)}
.nav-links .btn{padding:7px 14px}

/* hero */
.hero{top:100px;left:0;width:1200px;height:480px;background:var(--green)}
.hero h1{position:absolute;left:150px;top:110px;width:420px;color:var(--white);font-size:38px;line-height:1.2;font-weight:800}
.hero p{position:absolute;left:150px;top:258px;width:300px;color:#dff1e6;font-size:12px}
.hero .btn{position:absolute;left:150px;top:340px}
.hero-art{position:absolute;left:580px;top:30px;width:440px;height:400px;border-radius:10px;background:linear-gradient(160deg,#e9f3ec,#b9dcc6)}

/* audience cards */
.audience-card{top:612px;width:330px;height:240px;background:var(--white);border-radius:6px;box-shadow:0 6px 24px rgba(0,0,0,.1);text-align:center;padding-top:28px}
.audience-card .icon-art{width:90px;height:90px;margin:0 auto 14px;border-radius:50%}
.audience-card h3{font-size:16px;color:var(--ink);font-weight:700}
.audience-card p{font-size:11px;color:var(--muted);width:250px;margin:6px auto 0;line-height:1.5}

/* press */
.press-title{top:926px;left:0;width:1200px;font-size:11px;font-weight:700;color:var(--ink);letter-spacing:1px}
.press-row{top:990px;left:260px;width:680px;display:flex;justify-content:space-between}
.press-mark{width:90px;height:34px;border-radius:6px;background:#d8dbde}
.press-link{top:1056px;left:0;width:1200px;font-size:10px;color:var(--green)}

/* pink cta */
.cta{top:1140px;left:0;width:1200px;height:440px;background:var(--pink-pale)}
.cta h2{position:absolute;top:54px;left:220px;width:760px;text-align:center;color:var(--pink);font-size:24px;line-height:1.35;font-weight:700}
.cta h3{position:absolute;top:130px;left:0;width:1200px;text-align:center;color:var(--pink);font-style:italic;font-size:15px;font-weight:600}
.cta .body{position:absolute;top:190px;left:230px;width:740px;text-align:center;font-size:11px;line-height:1.7}
.cta .body2{position:absolute;top:262px;left:0;width:1200px;text-align:center;font-size:11px}
.cta .btn{position:absolute;top:328px;left:515px}

/* why */
.why-art{top:1680px;left:80px;width:400px;height:420px;border-radius:10px;background:linear-gradient(160deg,#f1f4f2,#d8e6dd)}
.why-label{top:1640px;left:562px}
.why h2{position:absolute;top:1670px;left:562px;width:360px;font-size:30px;line-height:1.2;color:var(--ink);font-weight:800}
.accordion{top:1790px;left:562px;width:376px}
.acc-item{border:1px solid var(--line);border-radius:3px;margin-bottom:12px;padding:12px 16px;font-size:12px;font-weight:700;color:var(--ink);display:flex;gap:10px;align-items:flex-start;background:var(--white)}
.acc-item.open{background:var(--green);color:var(--white);border-color:var(--green);flex-direction:column;gap:8px}
.acc-item.open p{font-weight:400;font-size:10.5px;color:#e3f4ea;line-height:1.6}
.acc-head{display:flex;gap:10px;align-items:center}
.chev{width:12px;height:12px;flex:none}

/* pricing */
.pricing-label{top:2200px;left:0;width:1200px}
.pricing h2{position:absolute;top:2224px;left:0;width:1200px;text-align:center;font-size:28px;font-weight:800;color:var(--ink)}
.plan{top:2288px;width:200px;height:372px;background:var(--white);border:1px solid var(--line);text-align:center;padding-top:26px}
.plan.featured{background:var(--green);border-color:var(--green);color:var(--white);top:2276px;height:396px;box-shadow:0 10px 26px rgba(47,158,94,.3)}
.plan h4{font-size:12px;font-weight:600;color:var(--ink)}
.plan.featured h4{color:var(--white)}
.price{font-size:42px;font-weight:700;color:var(--green);margin-top:18px;line-height:1}
.price sup{font-size:16px;vertical-align:top}
.price small{font-size:11px;font-weight:400}
.plan.featured .price{color:var(--white)}
.plan ul{list-style:none;font-size:10px;line-height:2.3;margin-top:22px;color:var(--muted)}
.plan.featured ul{color:#dff1e6}
.plan .btn{position:absolute;bottom:28px;left:30px;width:140px;text-align:center}
.plan.featured .btn{background:var(--white);color:var(--green)}

/* testimonials */
.testi-band{top:2768px;left:480px;width:680px;height:476px;background:var(--green)}
.testi-label{top:2800px;left:270px}
.testi h2{position:absolute;top:2826px;left:270px;width:200px;font-size:30px;line-height:1.2;color:var(--ink);font-weight:800}
.quote-mark{top:2960px;left:340px;width:70px;height:60px}
.testi-card{top:2964px;width:192px;height:256px;background:var(--white);padding:22px 18px;box-shadow:0 6px 20px rgba(0,0,0,.1);font-size:10.5px;line-height:1.7}
.testi-card .who{position:absolute;bottom:22px;left:18px;font-weight:700;color:var(--ink);font-size:10px}
.dots{top:3252px;left:528px;display:flex;gap:6px}
.dots span{width:8px;height:8px;border-radius:50%;background:#cfd4d7}
.dots span.on{background:var(--green)}

/* contact */
.contact{top:3350px;left:0;width:1200px;height:500px;background:var(--grey-bg)}
.contact .label{position:absolute;top:122px;left:0;width:1200px}
.contact h2{position:absolute;top:148px;left:0;width:1200px;text-align:center;font-size:26px;font-weight:800;color:var(--ink)}
.field{position:absolute;height:34px;background:var(--white);border:1px solid var(--line);font-size:10px;color:var(--muted);padding:9px 12px}
.contact .btn{position:absolute;top:460px;left:540px}

/* footer */
.footer{top:3860px;left:0;width:1200px;height:484px;background:var(--footer);color:#b8bdc1}
.footer .brand{position:absolute;top:60px;left:262px;color:var(--white)}
.footer .phone{position:absolute;top:108px;left:262px;font-family:"Montserrat",Arial,sans-serif;font-weight:700;color:var(--white);font-size:15px}
.footer .addr{position:absolute;top:138px;left:262px;font-size:10px;line-height:1.7}
.socials{position:absolute;top:200px;left:262px;display:flex;gap:10px}
.socials span{width:18px;height:18px;border-radius:50%;background:#5a6064}
.fcol{position:absolute;top:60px;font-size:10px;line-height:2.4}
.fcol h4{color:var(--white);font-size:12px;font-weight:700;margin-bottom:8px}
.footer-bottom{position:absolute;bottom:0;left:0;width:1200px;height:56px;background:var(--footer-bottom);text-align:center;font-size:10px;line-height:56px;color:#80868a}
</style>
</head>
<body>

<header class="abs site-nav">
  <div class="brand"><span class="brand-dot"></span>Dorvane</div>
  <nav class="nav-links">
    <span>Wie Funktioniert</span><span>Für Veranstalter</span><span>Speaker</span><span>Newsletter</span>
    <span class="btn btn-pink">Demo starten</span>
  </nav>
</header>

<section class="abs hero">
  <h1>Für die Picker:<br>picke nur Deine wichtigen Slides</h1>
  <p>Lass auch keine Idee im Vortrag verloren gehen – speichere Folien und Notizen direkt auf deinem Handy.</p>
  <span class="btn btn-pink">Mehr Erfahren</span>
  <div class="hero-art" role="img" aria-label="Illustration: people arranging slides on a large presentation screen"></div>
</section>

<article class="abs audience-card" style="left:258px">
  <div class="icon-art" role="img" aria-label="Illustration: colourful picker icon" style="background:linear-gradient(135deg,#f0567a,#f6b73c 50%,#3fb470)"></div>
  <h3>Für die Picker</h3>
  <p>Speichere Deine wichtigen Slides während des Vortrags und behalte Deine Notizen immer griffbereit.</p>
</article>
<article class="abs audience-card" style="left:612px">
  <div class="icon-art" role="img" aria-label="Illustration: speaker at a lectern" style="background:linear-gradient(135deg,#e9f6ee,#9fd1b2)"></div>
  <h3>Für die Speaker</h3>
  <p>Gewinne neue Leads aus Deinem Event und erhalte direkte Rückrufwünsche Deiner Zuhörer.</p>
</article>

<div class="abs press-title center">AS SEEN IN</div>
<div class="abs press-row">
  <span class="press-mark"></span><span class="press-mark"></span><span class="press-mark"></span><span class="press-mark"></span><span class="press-mark"></span><span class="press-mark"></span>
</div>
<div class="abs press-link center">Alle Berichte lesen</div>

<section class="abs cta">
  <h2>Willst Du qualifizierte Ergebnisse Deiner Marketing Events für die Weiterbearbeitung der Leads?</h2>
  <h3>dann teste den Dorvane Service für Dein Event!</h3>
  <p class="body">Dorvane ist die digitale Brücke zwischen Speaker und Publikum. Deine Zuhörer picken die Slides, die sie wirklich interessieren, und können Dich direkt um einen Rückruf bitten. So entstehen aus jedem Vortrag echte Leads, die Dein Vertrieb sofort weiterbearbeiten kann – ganz ohne Papier und Visitenkarten.</p>
  <p class="body2">Dein Event braucht nur einen QR-Code. Der Rest läuft im Browser jedes Smartphones.</p>
  <span class="btn btn-pink">Click here details</span>
</section>

<div class="abs why-art" role="img" aria-label="Illustration: people on a ladder beside a large phone showing slides"></div>
<div class="abs label why-label">Warum Dorvane</div>
<section class="why">
  <h2>Warum sollte ich Dorvane nutzen??</h2>
</section>
<div class="abs accordion">
  <div class="acc-item open">
    <div class="acc-head">
      <svg class="chev" viewBox="0 0 12 12"><path d="M2 4l4 4 4-4" fill="none" stroke="#fff" stroke-width="2"/></svg>
      Pick deine slides
    </div>
    <p>Mit einem Tipp speicherst Du jede Folie, die Dir wichtig ist. Alle gepickten Slides landen sortiert in Deiner Session und Du kannst sie später jederzeit wieder aufrufen, teilen oder mit dem Speaker besprechen.</p>
  </div>
  <div class="acc-item">
    <svg class="chev" viewBox="0 0 12 12"><path d="M4 2l4 4-4 4" fill="none" stroke="#2f9e5e" stroke-width="2"/></svg>
    No bad photos - please
  </div>
  <div class="acc-item">
    <svg class="chev" viewBox="0 0 12 12"><path d="M4 2l4 4-4 4" fill="none" stroke="#2f9e5e" stroke-width="2"/></svg>
    Erfasse deine Kommentare live während des Vortrags
  </div>
</div>

<div class="abs label pricing-label center">Unsere Preise</div>
<section class="pricing"><h2>Test Prior You Select</h2></section>
<article class="abs plan" style="left:272px">
  <h4>Basic</h4>
  <div class="price"><sup>€</sup>49<small>/mo</small></div>
  <ul><li>1 Event pro Monat</li><li>Bis 100 Teilnehmer</li><li>Slides speichern</li><li>E-Mail Support</li><li>Lead Export</li></ul>
  <span class="btn btn-green">Buy now</span>
</article>
<article class="abs plan featured" style="left:480px">
  <h4>Professional</h4>
  <div class="price"><sup>€</sup>149<small>/mo</small></div>
  <ul><li>5 Events pro Monat</li><li>Bis 500 Teilnehmer</li><li>Notizen und Kommentare</li><li>Rückruf Anfragen</li><li>Lead Export</li></ul>
  <span class="btn">Buy now</span>
</article>
<article class="abs plan" style="left:688px">
  <h4>Unlimited</h4>
  <div class="price"><sup>€</sup>199<small>/mo</small></div>
  <ul><li>Unbegrenzte Events</li><li>Alle Teilnehmer</li><li>Eigenes Branding</li><li>Priority Support</li><li>Lead Export</li></ul>
  <span class="btn btn-green">Buy now</span>
</article>

<div class="abs testi-band"></div>
<div class="abs label testi-label">Our Testimonials</div>
<section class="testi"><h2>Client Testimonials</h2></section>
<svg class="abs quote-mark" viewBox="0 0 70 60"><path d="M0 60V32C0 14 10 4 28 0v10C18 14 14 20 14 28h14v32zM42 60V32C42 14 52 4 70 0v10c-10 4-14 10-14 18h14v32z" fill="#e6ece8"/></svg>
<article class="abs testi-card" style="left:520px">
  <p>Die Zuhörer haben endlich alle wichtigen Folien auf dem Handy und wir bekommen nach dem Vortrag echte Rückrufwünsche statt leerer Visitenkarten.</p>
  <span class="who">– Sprecher</span>
</article>
<article class="abs testi-card" style="left:732px">
  <p>Die Einrichtung für unseren Kongress hat nur Minuten gedauert. Ein QR-Code auf der Leinwand reicht und alle Teilnehmer sind sofort dabei.</p>
  <span class="who">– Planung</span>
</article>
<article class="abs testi-card" style="left:944px">
  <p>Unser Vertrieb arbeitet jetzt direkt mit den Leads aus den Messevorträgen weiter. Das spart Zeit und bringt deutlich bessere Gespräche.</p>
  <span class="who">– Anna Berger</span>
</article>
<div class="abs dots"><span class="on"></span><span></span><span></span></div>

<section class="abs contact">
  <div class="label center">Kontakt</div>
  <h2>Sprich uns für eine Demo</h2>
  <div class="field" style="top:212px;left:312px;width:276px">Vorname</div>
  <div class="field" style="top:212px;left:608px;width:276px">Nachname</div>
  <div class="field" style="top:258px;left:312px;width:276px">E-Mail</div>
  <div class="field" style="top:258px;left:608px;width:276px">Telefon</div>
  <div class="field" style="top:304px;left:312px;width:572px;height:96px">Nachricht</div>
  <span class="btn btn-green">Get a quote</span>
</section>

<footer class="abs footer">
  <div class="brand"><span class="brand-dot"></span>Dorvane</div>
  <div class="phone">+49 700 55501234</div>
  <p class="addr">Musterweg 12, 88000 Süddorf<br>hallo@dorvane.net</p>
  <div class="socials"><span></span><span></span><span></span><span></span><span></span></div>
  <div class="fcol" style="left:436px">
    <h4>Useful Links</h4>
    <div>Über Uns</div><div>Für Veranstalter</div><div>Für Speaker</div><div>Preise</div><div>Kontakt</div>
  </div>
  <div class="fcol" style="left:600px">
    <h4>Footer Links</h4>
    <div>Impressum</div><div>Datenschutz</div><div>AGB</div><div>Cookies</div><div>Login</div>
  </div>
  <div class="fcol" style="left:780px;width:180px;line-height:1.6">
    <h4>Latest News</h4>
    <div>Neue Funktionen für Kongresse im Frühjahr</div><div style="color:#6f7579;margin-bottom:12px">April 2020</div>
    <div>Dorvane auf der Messe für Bildung</div><div style="color:#6f7579">März 2020</div>
  </div>
  <div class="footer-bottom">© 2020 Dorvane. Alle Rechte vorbehalten.</div>
</footer>

</body>
</html>
```